Golf Lesson Monthly Subscription Flyer

I need a flyer design for a monthly subscription golf lesson package. What's different about this package is that it includes live lessons, online lessons used for check ins, and a monthly subscription to my video paysite. I have 3 different tiers with different options in each tier. I need an easy to read flyer that I can email to my email list.

Target Market(s)

Golfers with excess money for lessons. Usually 50+ age

Colors

Designer to choose colors to be used in the design.

Requirements
Must have
• Needs to say "Cedar Hollow Coaching School" with the logo somewhere on the flyer.
• Also dale-pemberton.example needs to be on the flyer.

```html
<!DOCTYPE html>
<html lang="en">
<head>
<meta charset="utf-8">
<title>Cedar Hollow Coaching School – Monthly Subscriptions</title>
<link rel="stylesheet" href="https://fonts.googleapis.com/css2?family=Roboto+Condensed:wght@400;700&family=Montserrat:wght@400;600;700&display=swap">
<style>
  :root{
    --red:#e31e2a;
    --ink:#111111;
    --text:#1d1d1d;
    --paper:#ffffff;
    --stage:#e8e5e1;
    --sky:#c9ced6;
    --sky-deep:#aab3bf;
    --leaf:#4a8c2a;
    --rule:#c9c9c9;
  }
  *{box-sizing:border-box;margin:0;padding:0}
  html,body{width:1200px;height:1200px;overflow:hidden;background:var(--stage)}
  .flyer{position:absolute;left:172px;top:0;width:856px;height:1200px;background:var(--paper);overflow:hidden;font-family:"Montserrat",sans-serif;color:var(--text)}
  .hero-art{position:absolute;left:0;top:0;width:856px;height:620px}
  .abs{position:absolute}
  .head{font-family:"Roboto Condensed",sans-serif;font-weight:700;line-height:1}
  .title-main{left:38px;top:22px;font-size:72px;color:var(--red);letter-spacing:-0.5px}
  .title-sub{left:38px;top:96px;font-size:46px;color:var(--ink)}
  .cred{left:40px;font-family:"Roboto Condensed",sans-serif;font-weight:700;color:var(--ink);font-size:18px;line-height:23px}
  .cred .year{display:block;color:var(--red);font-size:31px;line-height:34px}
  .cred-name{top:162px}
  .cred-one{top:186px}
  .cred-two{top:290px}
  .badge{width:72px;height:72px;border-radius:50%}
  .badge-gold{left:255px;top:178px;background:#b89a5e;border:6px solid #1f2f4f}
  .badge-dark{left:254px;top:274px;background:#1b1b1b;border:5px solid #d94a2f}
  .brand-ring{left:110px;top:398px;width:200px;height:200px;border-radius:50%;background:var(--paper);border:6px solid var(--red);display:flex;align-items:center;justify-content:center;gap:10px}
  .brand-dot{width:16px;height:16px;border-radius:50%;background:var(--red);flex:none}
  .brand-name{font-family:"Montserrat",sans-serif;font-weight:400;font-size:20px;line-height:21px;color:var(--ink)}
  .intro{left:34px;top:608px;width:788px;text-align:center;font-size:13.4px;line-height:18.5px}
  .section-pill{left:178px;top:677px;width:500px;height:36px;border-radius:18px;background:var(--ink);color:#fff;display:flex;align-items:center;justify-content:center;font-family:"Roboto Condensed",sans-serif;font-weight:700;font-size:22px}
  .tier{top:726px;width:230px}
  .tier-1{left:26px}.tier-2{left:318px}.tier-3{left:607px}
  .tier-edge{position:absolute;left:0;top:0;width:3px;height:50px;background:linear-gradient(#fff,#c9c9c9)}
  .tier-tag{position:absolute;left:0;top:20px;width:82px;height:28px;background:var(--red);color:#fff;border-radius:0 14px 14px 0;font-family:"Roboto Condensed",sans-serif;font-weight:700;font-size:17px;line-height:28px;padding-left:12px}
  .tier-body{position:absolute;left:0;top:80px;width:240px;font-size:11.3px;line-height:15px}
  .point{display:flex;gap:5px;font-weight:700;margin-bottom:10px}
  .ball{flex:none;width:12px;height:12px;margin-top:1px}
  .detail{padding-left:18px;margin-bottom:28px}
  .rule{left:26px;top:1070px;width:802px;height:1px;background:var(--red)}
  .note{left:30px;top:1088px;font-weight:700;font-size:15px;line-height:20px;color:var(--ink)}
  .venue{left:760px;top:1096px;display:flex;align-items:center;gap:5px;font-family:"Montserrat",sans-serif;font-weight:700;font-size:8px;color:var(--leaf)}
  .venue i{width:12px;height:12px;border-radius:50%;background:var(--leaf);display:block}
  .footer{left:0;top:1134px;width:856px;height:66px}
  .footer-art{position:absolute;left:0;top:0}
  .book{left:40px;top:1143px;color:#fff;font-size:12.4px;line-height:20px}
  .book b{font-weight:700;padding-left:26px}
  .contact{top:1157px;color:#fff;font-size:12.4px;display:flex;align-items:center;gap:8px}
  .contact-mail{left:408px}
  .contact-phone{left:678px}
</style>
</head>
<body>
<main class="flyer">

  <svg class="hero-art" viewBox="0 0 856 620" width="856" height="620">
    <defs>
      <linearGradient id="skyFade" x1="0" x2="1" y1="0" y2="0">
        <stop offset="0.15" stop-color="#ffffff"/>
        <stop offset="0.55" stop-color="#d6dae0"/>
        <stop offset="1" stop-color="#b9c0ca"/>
      </linearGradient>
    </defs>
    <path role="img" aria-label="Photo of a golf coach in a red top finishing a swing against a cloudy sky"
          d="M120,0 H856 V220 C720,420 540,508 400,505 C320,503 260,485 215,455 C170,300 140,150 120,0 Z"
          fill="url(#skyFade)"/>
    <path d="M856,215 C720,420 540,510 400,507 C330,505 290,492 260,478 L300,548 C420,604 620,582 856,441 Z" fill="var(--red)"/>
    <path d="M0,304 Q45,368 122,404 L118,412 Q40,382 0,314 Z" fill="var(--red)"/>
  </svg>

  <h1 class="abs head title-main">CEDAR HOLLOW</h1>
  <h2 class="abs head title-sub">COACHING SCHOOL</h2>

  <p class="abs cred cred-name">DALE PEMBERTON, PGCA</p>
  <p class="abs cred cred-one"><span class="year">2016</span>UTAH SECTION PGCA<br>TEACHER OF THE YEAR</p>
  <p class="abs cred cred-two"><span class="year">2017-2018</span>FAIRWAY MONTHLY TOP<br>TEACHERS IN STATE LIST</p>

  <div class="abs badge badge-gold"></div>
  <div class="abs badge badge-dark"></div>

  <div class="abs brand-ring">
    <span class="brand-dot"></span>
    <span class="brand-name">DALE<br>PEMBERTON<br>GOLF</span>
  </div>

  <p class="abs intro">Learn from one of the best teaching pros in the state, Dale Pemberton, with this unique program which combines live lessons, structured practice, and online check-ins to help keep you accountable for your progress.</p>

  <div class="abs section-pill">GOLF LESSON MONTHLY SUBSCRIPTIONS</div>

  <section class="abs tier tier-1">
    <span class="tier-edge"></span><span class="tier-tag">TIER 1</span>
    <div class="tier-body">
      <p class="point"><svg class="ball" viewBox="0 0 12 12"><circle cx="6" cy="6" r="6" fill="#222"/><path d="M0,4H12M0,8H12M4,0V12M8,0V12" stroke="#fff" stroke-width="1"/></svg>Lessons with Dale's Assistant</p>
      <p class="detail">$400 a month<br>$1100 for 3 months<br>$2100 for 6 months</p>
      <p class="point"><svg class="ball" viewBox="0 0 12 12"><circle cx="6" cy="6" r="6" fill="#222"/><path d="M0,4H12M0,8H12M4,0V12M8,0V12" stroke="#fff" stroke-width="1"/></svg>Each month you get:</p>
      <p class="detail">2 90 min Lessons<br>Two 45 min practice sessions<br>45 min short game lesson<br>4 online checkins with Dale<br>+<br>3 month package gets 1 playing<br>lesson, 6 month package gets 3<br>playing lessons</p>
    </div>
  </section>

  <section class="abs tier tier-2">
    <span class="tier-edge"></span><span class="tier-tag">TIER 2</span>
    <div class="tier-body">
      <p class="point"><svg class="ball" viewBox="0 0 12 12"><circle cx="6" cy="6" r="6" fill="#222"/><path d="M0,4H12M0,8H12M4,0V12M8,0V12" stroke="#fff" stroke-width="1"/></svg>Same as above but Lessons<br>are with Dale</p>
      <p class="detail" style="margin-top:-4px">$600 a month<br>$1700 for 3 months<br>$3400 for 6 months</p>
      <p class="point"><svg class="ball" viewBox="0 0 12 12"><circle cx="6" cy="6" r="6" fill="#222"/><path d="M0,4H12M0,8H12M4,0V12M8,0V12" stroke="#fff" stroke-width="1"/></svg>Each month you get:</p>
      <p class="detail">2 90 min Lessons<br>Two 45 min practice sessions<br>45 min short game lesson<br>4 online checkins with Dale<br>+<br>3 month package gets 1 playing<br>lesson, 6 month package gets 3<br>playing lessons</p>
    </div>
  </section>

  <section class="abs tier tier-3">
    <span class="tier-edge"></span><span class="tier-tag">TIER 3</span>
    <div class="tier-body">
      <p class="point"><svg class="ball" viewBox="0 0 12 12"><circle cx="6" cy="6" r="6" fill="#222"/><path d="M0,4H12M0,8H12M4,0V12M8,0V12" stroke="#fff" stroke-width="1"/></svg>Lessons</p>
      <p class="detail">$800 a month<br>$2300 for 3 months<br>$4500 for 6 months</p>
      <p class="point"><svg class="ball" viewBox="0 0 12 12"><circle cx="6" cy="6" r="6" fill="#222"/><path d="M0,4H12M0,8H12M4,0V12M8,0V12" stroke="#fff" stroke-width="1"/></svg>Each month you get:</p>
      <p class="detail">Four 90 min lessons<br>Four 45 min practice sessions<br>Four Online Checkins<br>+<br>3 month package gets 1 playing<br>lesson, 6 month package gets 3<br>playing lessons</p>
    </div>
  </section>

  <div class="abs rule"></div>
  <p class="abs note">Payments for 3 month or 6 month packages<br>can be broken down into payments per month</p>
  <div class="abs venue"><i></i>CEDAR HOLLOW</div>

  <div class="abs footer">
    <svg class="footer-art" viewBox="0 0 856 66" width="856" height="66">
      <rect width="856" height="66" fill="var(--ink)"/>
      <path d="M0,0 H350 Q335,6 348,14 Q362,30 336,66 H0 Z" fill="var(--red)"/>
    </svg>
  </div>
  <p class="abs book">To schedule or for other questions<br><b>Website dale-pemberton.example</b></p>
  <p class="abs contact contact-mail">
    <svg width="18" height="12" viewBox="0 0 18 12"><rect width="18" height="12" fill="var(--red)"/><path d="M0,0 L9,7 L18,0" fill="none" stroke="#111" stroke-width="1.4"/></svg>
    dalepembertongolf@example.com
  </p>
  <p class="abs contact contact-phone">
    <svg width="12" height="18" viewBox="0 0 12 18"><path d="M3,0 L6,4 L4,6 Q5,10 8,12 L10,10 L12,14 L9,18 Q1,14 0,3 Z" fill="var(--red)"/></svg>
    555-014-2297
  </p>

</main>
</body>
</html>
```